Help me make landing pages for my web application that are mobile friendly

I need to make 2 mobile friendly landing pages for an application. The 2 pages will be related. First I need a home page and then I need a working page. I do not want to change the color scheme or logos. Just layout and design.

```html
<!DOCTYPE html>
<html lang="en">
<head>
<meta charset="utf-8">
<title>TeachCover – My Assignments</title>
<link href="https://fonts.googleapis.com/css2?family=Nunito:wght@400;500;600;700&display=swap" rel="stylesheet">
<style>
:root{
  --page:#ffffff;
  --list-bg:#f6f6f7;
  --card:#ffffff;
  --brand:#6a4fb6;
  --accent:#1daed6;
  --text:#262626;
  --muted:#8a8a8a;
  --tab:#8e8e8e;
  --chip:#efeff0;
  --active-bg:#e4f4e9;--active-fg:#3f8c5b;
  --done-bg:#e1f0fb;--done-fg:#2a9ad2;
  --cancel-bg:#fae5ea;--cancel-fg:#8d4b5b;
}
*{box-sizing:border-box;margin:0;padding:0}
html,body{width:1200px;height:1110px;overflow:hidden;background:var(--page);font-family:"Nunito",sans-serif;color:var(--text)}
.screen{position:absolute;top:109px;width:472px;height:772px;border-radius:34px;overflow:hidden;background:var(--list-bg);box-shadow:0 0 0 1px #e6e6e6}
.screen--home{left:76px}
.screen--work{left:634px}
.app-header{position:absolute;left:0;top:0;width:100%;height:165px;background:#fff;z-index:2}
.screen--work .app-header{height:110px;box-shadow:0 2px 6px rgba(0,0,0,.04)}
.brand{position:absolute;left:24px;top:66px;display:flex;align-items:center;gap:9px;font-weight:600;font-size:25px;color:var(--brand)}
.brand-dot{width:22px;height:22px;border-radius:50%;background:var(--brand)}
.logout{position:absolute;right:30px;top:69px}
.tabs{position:absolute;left:22px;display:flex;gap:34px;font-size:14px;letter-spacing:1px;color:var(--tab);white-space:nowrap}
.screen--home .tabs{top:126px}
.screen--work .tabs{top:72px;left:21px}
.tab--current{color:var(--brand);position:relative}
.tab--current::after{content:"";position:absolute;left:0;right:0;bottom:-14px;height:2px;background:var(--brand)}
.card{position:absolute;left:21px;width:427px;height:239px;background:var(--card);border-radius:10px}
.avatar{position:absolute;left:31px;top:29px;width:60px;height:60px;border-radius:50%}
.av1{background:radial-gradient(circle at 50% 40%,#c9a48d,#3a3f4a 75%)}
.av2{background:radial-gradient(circle at 50% 40%,#d9b39a,#6b8fb0 75%)}
.av3{background:radial-gradient(circle at 50% 40%,#c4a08a,#555a60 75%)}
.edit{position:absolute;left:51px;top:108px}
.label{position:absolute;font-size:13px;color:var(--muted)}
.value{position:absolute;font-size:15px}
.name{position:absolute;left:115px;top:47px;font-size:15.5px;font-weight:600;color:var(--accent)}
.l-sub{left:115px;top:24px}.l-status{left:270px;top:24px}
.role{left:115px;top:71px}
.l-loc{left:115px;top:107px}.loc{left:115px;top:130px}
.l-time{left:115px;top:165px}
.chips{position:absolute;left:115px;top:187px;display:flex;gap:6px}
.chip{height:29px;line-height:29px;padding:0 11px;border-radius:15px;background:var(--chip);font-size:12.5px;letter-spacing:1px}
.status{position:absolute;left:270px;top:46px;height:29px;line-height:29px;padding:0 12px;border-radius:15px;font-size:12.5px;letter-spacing:1.4px}
.s-active{background:var(--active-bg);color:var(--active-fg)}
.s-done{background:var(--done-bg);color:var(--done-fg)}
.s-cancel{background:var(--cancel-bg);color:var(--cancel-fg)}
</style>
</head>
<body>

<svg width="0" height="0" style="position:absolute">
  <defs>
    <g id="pencil" fill="none" stroke="#1daed6" stroke-width="1.4" stroke-linecap="round" stroke-linejoin="round">
      <path d="M4 14 L4.6 10.6 L12.6 2.6 a1.5 1.5 0 0 1 2.1 0 l0.7 0.7 a1.5 1.5 0 0 1 0 2.1 L7.4 13.4 Z"/>
      <path d="M1 18 H17"/>
    </g>
  </defs>
</svg>

<!-- Home screen -->
<section class="screen screen--home">
  <header class="app-header">
    <div class="brand"><span class="brand-dot"></span>TeachCover</div>
    <svg class="logout" width="28" height="28" viewBox="0 0 28 28" fill="none" stroke="#6a4fb6" stroke-width="1.6" stroke-linecap="round" stroke-linejoin="round">
      <path d="M1 9 V1 H27 V27 H1 V19"/><path d="M3 14 H18"/><path d="M13 9 L18 14 L13 19"/>
    </svg>
    <nav class="tabs"><span class="tab--current">MY ASSIGNMENT</span><span>AVAILABLE OPENINGS</span><span>OTHER MEMBERS</span></nav>
  </header>

  <article class="card" style="top:193px">
    <div class="avatar av1" role="img" aria-label="Portrait photo of the absent teacher"></div>
    <svg class="edit" width="20" height="20"><use href="#pencil"/></svg>
    <span class="label l-sub">Subbing for :</span><span class="name">Owen Harper</span><span class="value role">Teacher</span>
    <span class="label l-status">Status :</span><span class="status s-active">ACTIVE</span>
    <span class="label l-loc">Location :</span><span class="value loc">Demo Valley Elementary Schools</span>
    <span class="label l-time">Time Slots :</span>
    <div class="chips"><span class="chip">09/02 - 09/18</span><span class="chip">1h : 20m</span></div>
  </article>

  <article class="card" style="top:450px">
    <div class="avatar av2" role="img" aria-label="Portrait photo of the absent teacher"></div>
    <svg class="edit" width="20" height="20"><use href="#pencil"/></svg>
    <span class="label l-sub">Subbing for :</span><span class="name">Clara Whitfield</span><span class="value role">Teacher</span>
    <span class="label l-status">Status :</span><span class="status s-done">COMPLETED</span>
    <span class="label l-loc">Location :</span><span class="value loc">Demo Valley Elementary Schools</span>
    <span class="label l-time">Time Slots :</span>
    <div class="chips"><span class="chip">09/02 - 09/18</span><span class="chip">1h : 20m</span></div>
  </article>

  <article class="card" style="top:708px">
    <div class="avatar av3" role="img" aria-label="Portrait photo of the staff member"></div>
    <span class="label l-sub">Subbing for :</span><span class="name">Extra Duty</span>
    <span class="label l-status">Status :</span><span class="status s-cancel">CANCELED</span>
  </article>
</section>

<!-- Working screen (scrolled list) -->
<section class="screen screen--work">
  <header class="app-header">
    <nav class="tabs"><span class="tab--current">MY ASSIGNMENT</span><span>AVAILABLE OPENINGS</span><span>OTHER MEMBERS</span></nav>
  </header>

  <article class="card" style="top:35px">
    <div class="avatar av1" role="img" aria-label="Portrait photo of the absent teacher"></div>
    <svg class="edit" width="20" height="20"><use href="#pencil"/></svg>
    <span class="value role">Teacher</span>
    <span class="label l-loc">Location :</span><span class="value loc">Demo Valley Elementary Schools</span>
    <span class="label l-time">Time Slots :</span>
    <div class="chips"><span class="chip">09/02 - 09/18</span><span class="chip">1h : 20m</span></div>
  </article>

  <article class="card" style="top:293px">
    <div class="avatar av2" role="img" aria-label="Portrait photo of the absent teacher"></div>
    <svg class="edit" width="20" height="20"><use href="#pencil"/></svg>
    <span class="label l-sub">Subbing for :</span><span class="name">Clara Whitfield</span><span class="value role">Teacher</span>
    <span class="label l-status">Status :</span><span class="status s-done">COMPLETED</span>
    <span class="label l-loc">Location :</span><span class="value loc">Demo Valley Elementary Schools</span>
    <span class="label l-time">Time Slots :</span>
    <div class="chips"><span class="chip">09/02 - 09/18</span><span class="chip">1h : 20m</span></div>
  </article>

  <article class="card" style="top:551px">
    <div class="avatar av3" role="img" aria-label="Portrait photo of the staff member"></div>
    <svg class="edit" width="20" height="20"><use href="#pencil"/></svg>
    <span class="label l-sub">Subbing for :</span><span class="name">Extra Duty</span><span class="value role">Teacher</span>
    <span class="label l-status">Status :</span><span class="status s-cancel">CANCELED</span>
    <span class="label l-loc">Location :</span><span class="value loc">Demo Valley Elementary Schools</span>
    <span class="label l-time">Time Slots :</span>
    <div class="chips"><span class="chip">09/02 - 09/18</span><span class="chip">1h : 20m</span></div>
  </article>
</section>

</body>
</html>
```